Adventurous female pilot

I am looking for a personal business card, for a very well qualified female pilot, with a lot of aviation experience.

Currently an airline pilot, have worked as a bush pilot in Africa, looking to get into corporate aviation, or private jet owners.
Want a classy looking card for networking...

Could be interested in a retro\vintage look also?!

An idea,, is an african sunset background, with my wings\logo on it
Updates

I just want to say thank you to all of your for your amazing designs!

I have been very busy flying this past week , so not had a chance to be on the computer much.
But I provide some feedback, and conclusions very soon!
Thank you again.

Marla

Reason: Still waiting on a couple of revisions to be 100% about my choice!

Target Market(s)

corporate aviation, private jet owners, casino's,
General audience.
networking

Industry/Entity Type

Airline

Requirements
Nice to have
• Classy, edgy, sexy, but also feminine

```html
<!DOCTYPE html>
<html lang="en">
<head>
<meta charset="utf-8">
<title>Marla Keller – Business Card</title>
<link rel="stylesheet" href="https://fonts.googleapis.com/css2?family=Arvo:wght@400;700&display=swap">
<style>
  :root {
    --sky-top: #3d0805;
    --sky-upper: #6a230a;
    --sky-mid: #8a4a0c;
    --sky-lower: #9a560e;
    --sun-core: #c98a1a;
    --sun-edge: rgba(190, 120, 20, 0);
    --haze: rgba(60, 20, 5, 0.55);
    --ground: #060302;
    --text: #ffffff;
    --mark: #e4e4e4;
    --shadow: rgba(0, 0, 0, 0.9);
  }
  html, body {
    margin: 0;
    padding: 0;
    width: 1200px;
    height: 660px;
    overflow: hidden;
    background: #ffffff;
  }
  .card {
    position: relative;
    width: 1200px;
    height: 660px;
    overflow: hidden;
    font-family: "Arvo", Georgia, serif;
    color: var(--text);
  }
  .sunset-scene {
    position: absolute;
    inset: 0;
    background:
      radial-gradient(ellipse 200px 190px at 600px 190px, var(--sun-core) 0%, var(--sun-core) 55%, var(--sun-edge) 100%),
      radial-gradient(ellipse 700px 320px at 600px 260px, rgba(170, 100, 15, 0.55) 0%, rgba(170, 100, 15, 0) 100%),
      linear-gradient(to bottom, rgba(0,0,0,0) 0%, rgba(0,0,0,0) 66%, var(--haze) 76%, var(--ground) 88%, var(--ground) 100%),
      linear-gradient(
        to bottom,
        var(--sky-top) 0%,
        var(--sky-upper) 20%,
        var(--sky-mid) 38%,
        var(--sky-lower) 60%,
        var(--sky-mid) 72%,
        var(--ground) 90%
      );
  }
  .brand-mark {
    position: absolute;
    top: 88px;
    left: 0;
    width: 100%;
    margin: 0;
    text-align: center;
    font-size: 66px;
    line-height: 84px;
    font-weight: 400;
    color: var(--mark);
    letter-spacing: 3px;
  }
  .contact {
    position: absolute;
    top: 320px;
    left: 0;
    width: 100%;
    text-align: center;
    text-shadow: 3px 4px 5px var(--shadow);
  }
  .contact__name {
    margin: 0;
    font-size: 79px;
    font-weight: 400;
    line-height: 96px;
    letter-spacing: 1px;
  }
  .contact__line {
    margin: 0;
    font-size: 43px;
    line-height: 58px;
    font-weight: 400;
  }
</style>
</head>
<body>
  <div class="card">
    <div class="sunset-scene" role="img" aria-label="African savanna at sunset with a large glowing sun, acacia trees and silhouettes of zebra, elephant and giraffe"></div>

    <p class="brand-mark">Keller Wings</p>

    <div class="contact">
      <h1 class="contact__name">Marla Keller</h1>
      <p class="contact__line">Email: marlackeller@skyroute.net</p>
      <p class="contact__line">Cell US: +1 702-555-0148</p>
      <p class="contact__line">Cell Taipei: +886 970-555-312</p>
    </div>
  </div>
</body>
</html>
```